M Zyvantics Buisness Cards

I need a technology focused clean business card for my employees. I have attached out logo to include in the mocks. We're a modern tech consulting firm that drives to interface humanity with technology in a truly cohesive fashion.

```html
<!DOCTYPE html>
<html lang="en">
<head>
<meta charset="utf-8">
<title>M Zyvantics Business Cards</title>
<link href="https://fonts.googleapis.com/css2?family=Open+Sans:wght@400;600;700&display=swap" rel="stylesheet">
<style>
  :root {
    --backdrop: #2b2e33;
    --card-white: #ffffff;
    --brand-blue: #1f6fc4;
    --brand-blue-light: #2a86d6;
    --ink-dark: #2a2a2c;
    --ink-grey: #6d6e71;
    --band-dark: #262628;
    --band-text: #f2f2f2;
  }
  * { margin: 0; padding: 0; box-sizing: border-box; }
  html, body {
    width: 1200px; height: 900px; overflow: hidden;
    background: var(--backdrop);
    font-family: "Open Sans", Arial, sans-serif;
  }
  .sheet { position: relative; width: 1200px; height: 900px; }
  .card {
    position: absolute; left: 240px; width: 720px; height: 400px;
    background: var(--card-white); border-radius: 26px; overflow: hidden;
  }
  .card--front { top: 40px; }
  .card--back { top: 460px; }
  .card svg.shapes { position: absolute; inset: 0; }

  .brand {
    position: absolute; display: flex; align-items: center; gap: 14px;
  }
  .brand__dot {
    width: 34px; height: 34px; border-radius: 50%; background: var(--brand-blue);
  }
  .brand__name {
    font-weight: 700; color: var(--ink-grey); letter-spacing: 1px;
  }
  .card--front .brand { left: 0; right: 0; top: 140px; justify-content: center; }
  .card--front .brand__name { font-size: 54px; }
  .card--front .website {
    position: absolute; left: 0; right: 0; top: 228px; text-align: center;
    color: var(--brand-blue); font-size: 17px; letter-spacing: 3px;
  }

  .card--back .brand { left: 48px; top: 34px; }
  .card--back .brand__dot { width: 26px; height: 26px; }
  .card--back .brand__name { font-size: 38px; }

  .info-band {
    position: absolute; left: 0; right: 0; top: 150px; height: 112px;
    background: var(--band-dark); color: var(--band-text);
    display: flex; align-items: center; padding: 0 40px; gap: 40px;
  }
  .person { width: 180px; }
  .person__name { font-weight: 700; font-size: 19px; letter-spacing: .5px; }
  .person__title { color: var(--brand-blue-light); font-size: 15px; }
  .contact-list { list-style: none; display: flex; flex-direction: column; gap: 12px; font-size: 15px; }
  .contact-list li { display: flex; align-items: center; gap: 10px; }
  .icon { width: 22px; height: 22px; flex: none; }
  .address {
    position: absolute; left: 250px; top: 296px; display: flex; align-items: center; gap: 10px;
    font-size: 16px; color: var(--ink-dark);
  }
</style>
</head>
<body>
<main class="sheet">

  <section class="card card--front" aria-label="Business card front">
    <svg class="shapes" width="720" height="400" viewBox="0 0 720 400">
      <path d="M470 0 H720 V95 C700 40 640 28 560 22 C520 18 490 12 470 0 Z" fill="var(--brand-blue)"/>
      <path d="M0 330 C120 340 220 345 300 400 H0 Z" fill="var(--brand-blue)"/>
    </svg>
    <div class="brand">
      <span class="brand__dot"></span>
      <span class="brand__name">M Zyvantics</span>
    </div>
    <p class="website">www.yourwebsite.com</p>
  </section>

  <section class="card card--back" aria-label="Business card back">
    <svg class="shapes" width="720" height="400" viewBox="0 0 720 400">
      <path d="M720 0 V150 H520 C560 140 560 90 600 70 C650 45 700 40 720 0 Z" fill="var(--brand-blue)"/>
      <path d="M0 262 H70 C100 300 80 360 40 400 H0 Z" fill="var(--brand-blue)"/>
      <rect x="0" y="388" width="720" height="12" fill="var(--brand-blue)"/>
    </svg>
    <div class="brand">
      <span class="brand__dot"></span>
      <span class="brand__name">M Zyvantics</span>
    </div>

    <div class="info-band">
      <div class="person">
        <p class="person__name">YOUR NAME</p>
        <p class="person__title">Job Title</p>
      </div>
      <ul class="contact-list">
        <li>
          <svg class="icon" viewBox="0 0 24 24"><circle cx="12" cy="12" r="11" fill="none" stroke="var(--brand-blue-light)" stroke-width="1.6"/><path d="M8 6.5l2 2-1 1.5c.8 1.8 2.2 3.2 4 4l1.5-1 2 2-1.5 2C11 16.5 7.5 13 6.5 8z" fill="var(--brand-blue-light)"/></svg>
          000 000 0000
        </li>
        <li>
          <svg class="icon" viewBox="0 0 24 24"><circle cx="12" cy="12" r="11" fill="none" stroke="var(--brand-blue-light)" stroke-width="1.6"/><rect x="8.5" y="6" width="7" height="12" rx="1.2" fill="none" stroke="var(--brand-blue-light)" stroke-width="1.6"/></svg>
          000 000 0000
        </li>
      </ul>
      <ul class="contact-list">
        <li>
          <svg class="icon" viewBox="0 0 24 24"><circle cx="12" cy="12" r="11" fill="none" stroke="var(--brand-blue-light)" stroke-width="1.6"/><rect x="6.5" y="7" width="11" height="8" rx="1" fill="none" stroke="var(--brand-blue-light)" stroke-width="1.6"/><path d="M10 17.5h4" stroke="var(--brand-blue-light)" stroke-width="1.6"/></svg>
          www.yourwebsite.com
        </li>
        <li>
          <svg class="icon" viewBox="0 0 24 24"><circle cx="12" cy="12" r="11" fill="none" stroke="var(--brand-blue-light)" stroke-width="1.6"/><rect x="6.5" y="8" width="11" height="8" fill="var(--brand-blue-light)"/><path d="M6.5 8l5.5 4.5L17.5 8" fill="none" stroke="var(--band-dark)" stroke-width="1.2"/></svg>
          info@youremail.com
        </li>
      </ul>
    </div>

    <p class="address">
      <svg class="icon" viewBox="0 0 24 24"><circle cx="12" cy="12" r="11" fill="none" stroke="var(--brand-blue)" stroke-width="1.6"/><path d="M12 5.5a4 4 0 0 0-4 4c0 3 4 8 4 8s4-5 4-8a4 4 0 0 0-4-4z" fill="var(--brand-blue)"/><circle cx="12" cy="9.5" r="1.5" fill="#fff"/></svg>
      000, Any Street, Any City, ST 00000
    </p>
  </section>

</main>
</body>
</html>
```